Monthly Mailed Newsletter/Magazine for Medical Spa

Every month we send out a mailed newsletter/magazine to our visitors from the previous month. We made a sample newsletter/magazine as a guideline of what we are looking for. We need a designer to make a simple and clean design layout.

- Attached is our sample design that has all the content we want to use.
- Newsletter/magazine is 8 pages total.
- Size of each page is 8.5 inches in width by 11 inches in height.
- Content and images can be located here: https://files.vornacloud.net/shared/8kqTRw3ZpLmX2vNcA7yHd5EbJ0sUgFo4e?view=open

The following will give you an idea of our brand presentation.
Our website is: www.GlowDermaClinic.com
Our Instagram; @glowdermaclinic
Our Facebook: www.socialtreo.com/glowdermaclinic

Target Market(s)

Women 25 - 45

Industry/Entity Type

Beauty

Font styles to use
Other font styles liked:
• Josefins Sans Bold & Lato

Colors
f78f20
ffffff

Requirements
Must have
• - Our Logo
- Our tagline: YOUR SKIN DESERVES IT!
- Address and contact information for our locations
- Our color scheme: Black and #FAA641
- Heading font is Josefin Sans Bold
- Paragraph font is Lato
- Our website address: www.GlowDermaClinic.com

```html
<!DOCTYPE html>
<html lang="en">
<head>
<meta charset="utf-8">
<title>Glow Derma Clinic Newsletter Spread</title>
<link rel="stylesheet" href="https://fonts.googleapis.com/css2?family=Josefin+Sans:ital,wght@0,400;0,600;0,700;1,600&family=Lato:wght@400;700&display=swap">
<style>
  :root{
    --backdrop:#ebe2de;
    --paper:#ffffff;
    --ink:#1c1c1c;
    --orange:#faa641;
    --orange-deep:#f0993a;
    --white:#ffffff;
  }
  *{box-sizing:border-box;margin:0;padding:0}
  html,body{width:1200px;height:833px;overflow:hidden;background:var(--backdrop)}
  body{font-family:'Josefin Sans',sans-serif;color:var(--ink)}
  .spread{position:absolute;left:20px;top:40px;width:1160px;height:752px;display:flex;box-shadow:0 10px 24px rgba(0,0,0,.12)}
  .page{position:relative;width:580px;height:752px;background:var(--paper);overflow:hidden}
  .page--left{border-right:1px solid #ddd}

  .brand{position:absolute;top:22px;right:20px;display:flex;align-items:center;gap:7px}
  .brand__dot{width:26px;height:26px;border-radius:50%;background:var(--orange)}
  .brand__name{font-family:'Josefin Sans',sans-serif;font-weight:700;font-size:21px;color:var(--ink);line-height:1}

  .photo{position:absolute}
  .photo--hero{left:0;top:66px;width:580px;height:300px;background:linear-gradient(90deg,#a89d92 0%,#a89d92 42%,#c39478 62%,#b7886d 100%)}
  .hero-title{position:absolute;left:36px;top:160px;width:200px;font-style:italic;font-weight:600;font-size:22px;line-height:1.25;color:var(--ink)}

  .section-title{font-style:italic;font-weight:600;font-size:16px;line-height:1.3}
  .rule{display:block;height:5px;background:var(--orange-deep);margin:5px 0 9px}
  .body-copy{font-size:12.3px;line-height:1.38}

  .article--intro{position:absolute;left:32px;top:384px;width:250px}
  .article--intro .rule{width:118px}

  .callout{position:absolute;background:var(--orange);color:var(--white)}
  .callout--risk{left:302px;top:400px;width:254px;padding:12px 12px 14px;font-size:12.3px;line-height:1.4}

  .footer{position:absolute;left:18px;right:16px;bottom:28px;height:28px;background:var(--orange-deep);display:flex;align-items:center;justify-content:space-between;padding:0 10px;color:var(--white)}
  .footer__url{font-size:13px;font-weight:400}
  .footer__tagline{font-size:14px;font-weight:700;letter-spacing:.3px}

  .article--compare{position:absolute;left:26px;top:44px;width:248px}
  .article--compare .section-title{font-size:15.5px;width:210px}
  .article--compare .rule{width:116px;margin-bottom:10px}
  .article--compare .body-copy{font-size:12px;line-height:1.37}

  .photo--legs{left:290px;top:66px;width:270px;height:212px;background:linear-gradient(160deg,#d8d4cf 0%,#9a9792 45%,#d9b39d 75%,#8e8c89 100%)}
  .photo--budget{left:292px;top:322px;width:272px;height:214px;background:linear-gradient(170deg,#e8e6e3 0%,#c7b9d6 30%,#7c93ad 55%,#b98a5c 100%)}

  .callout--advice{left:28px;top:490px;width:252px;height:190px;padding:12px 12px}
  .callout__title{font-weight:600;font-size:15px;color:var(--white)}
  .callout__rule{display:block;width:122px;height:4px;background:var(--white);margin:4px 0 10px}
  .callout__text{font-size:12px;line-height:1.38;color:var(--white)}
</style>
</head>
<body>
<main class="spread">
  <section class="page page--left">
    <div class="brand"><span class="brand__dot"></span><span class="brand__name">Glow Derma Clinic</span></div>
    <div class="photo photo--hero" role="img" aria-label="Woman using an at-home laser hair removal device on her leg"></div>
    <h1 class="hero-title">Do at-home laser hair removal gadgets work?</h1>

    <article class="article article--intro">
      <h2 class="section-title">Do at-home laser hair removal gadgets work?</h2>
      <span class="rule"></span>
      <p class="body-copy">NYC's dermatology professionals answer the million-dollar question with a very cautionary yes. Dr. Arman Velcourt claims that results vary according to individuals. Success is dependant on the contrast between your hair and skin color. Light skin and dark hair produce the best outcomes, while other combinations can prove them ineffective. Generally, at-home products are more suitable for use on smaller areas such as your lip and underarms. They can also be beneficial for maintenance after in-office treatments. Are there any risks involved?</p>
    </article>

    <aside class="callout callout--risk">
      There is a risk of hyperpigmentation and skin damage if the device is used inappropriately. Although so, LUMEN Medspa esthetician, Mara Linden claims that FDA approved home devices are generally safe. She said that they are however not as effective as in-office treatments. It is important to thoroughly understand the product before using it. For example, most products are not suitable for breastfeeding or pregnant mothers.
    </aside>

    <footer class="footer"><span class="footer__url">www.GlowDermaClinic.com</span><span class="footer__tagline">YOUR SKIN DESERVES IT!</span></footer>
  </section>

  <section class="page page--right">
    <div class="brand"><span class="brand__dot"></span><span class="brand__name">Glow Derma Clinic</span></div>

    <article class="article article--compare">
      <h2 class="section-title">Is there a difference in the effectiveness of at-home versus inoffice hair removal treatment?</h2>
      <span class="rule"></span>
      <p class="body-copy">The consensus across the board of professionals is a resounding yes! Laser hair removal is an extremely targeted treatment. It requires calibrated settings that account for both your hair and skin color. Because of safety concerns, most DIY gadgets use Intense Pulse Light (IPL) which is comparatively underpowered and not as effective as a visit to a specialist. Furthermore, with IPL, the less contrast you have between your hair and skin pigment, the higher the risk of skin damage. If you're melanin-blessed, it's best to stay away from at-home devices and seek professional treatment. The difference being, they know what are doing, and can treat all skin tones!</p>
    </article>

    <div class="photo photo--legs" role="img" aria-label="Woman seated on a rug using a handheld hair removal device on her lower leg"></div>
    <div class="photo photo--budget" role="img" aria-label="Woman sitting on a wooden floor with a notebook and calculator reviewing paperwork"></div>

    <aside class="callout callout--advice">
      <h3 class="callout__title">A last word of advice?</h3>
      <span class="callout__rule"></span>
      <p class="callout__text">No matter which you choose, it's important to avoid, tweezing hairs, tanning lotions, antibiotics, and retinoids two weeks prior and post-treatment. Life is too short for anyone to be at war with hair woes. If you don't use it, just lose it</p>
    </aside>

    <footer class="footer"><span class="footer__url">www.GlowDermaClinic.com</span><span class="footer__tagline">YOUR SKIN DESERVES IT!</span></footer>
  </section>
</main>
</body>
</html>
```